Business Card for Yachting Management Company

Need a business card design for a new yachting project management company. Attached is the logo for the company.
Our clients are large yacht owners and captains.
Design must be in the style of the logo. Modern, elegant.

Example of data to show:
Peter Hollis
Project Manager
(+34) 612 738 104
peter@quorvane.net
Quorvane Management - Meridel Tower, Office 22 - KRB - Palma de Mallorca

The data above will have to be changed (by me) for the different people in the company over the next years.

Will be printed using PrintNova (Lustre Card Series). They provide these guidelines for the size:
"the actual size of the card is 1050 x 600 pixels. However, the full bleed size is 1083 x 633 pixels, and the safe printing area is 1008 x 558 pixels."

```html
<!DOCTYPE html>
<html lang="en">
<head>
<meta charset="utf-8">
<title>Quorvane Management – Business Card</title>
<link rel="stylesheet" href="https://fonts.googleapis.com/css2?family=Michroma&family=Arimo:wght@400;700&display=swap">
<style>
  :root {
    --backdrop: #878787;
    --card-white: #ffffff;
    --brand-blue: #0071bc;
    --stripe-grey: #878787;
    --text-grey: #6d6d6d;
    --card-shadow: #1a1a1a;
  }
  * { box-sizing: border-box; margin: 0; padding: 0; }
  html, body {
    width: 1075px;
    height: 1200px;
    overflow: hidden;
    background: var(--backdrop);
  }
  .canvas {
    position: relative;
    width: 1075px;
    height: 1200px;
  }
  .card {
    position: absolute;
    width: 661px;
    height: 393px;
    border-radius: 22px;
    overflow: hidden;
    box-shadow: 3px 3px 0 var(--card-shadow);
  }
  .card--front {
    left: 207px;
    top: 187px;
    background: var(--card-white);
  }
  .card--back {
    left: 203px;
    top: 638px;
    background: var(--brand-blue);
  }
  .front-stripes {
    position: absolute;
    inset: 0;
    width: 661px;
    height: 393px;
  }
  .stripe--blue { fill: var(--brand-blue); }
  .stripe--grey { fill: var(--stripe-grey); }

  .contact {
    position: absolute;
    left: 42px;
    top: 152px;
    font-family: "Arimo", Arial, sans-serif;
    color: var(--text-grey);
    font-size: 18px;
    line-height: 24px;
  }
  .contact__name {
    font-family: "Michroma", sans-serif;
    font-weight: 400;
    font-size: 20px;
    line-height: 26px;
    color: var(--brand-blue);
    text-transform: uppercase;
    letter-spacing: 0.5px;
  }
  .contact__title { margin-top: -3px; }
  .contact__lines { margin-top: 12px; }
  .contact__line {
    display: flex;
    align-items: center;
    gap: 6px;
  }
  .contact__icon { width: 16px; height: 16px; fill: var(--brand-blue); }
  .contact__company {
    margin-top: 12px;
    font-weight: 700;
    color: var(--brand-blue);
  }

  .back-field {
    position: absolute;
    inset: 0;
    background: var(--brand-blue);
  }
  .wordmark {
    position: absolute;
    left: 0;
    right: 0;
    top: 50%;
    transform: translateY(-50%);
    text-align: center;
    font-family: "Michroma", sans-serif;
    font-weight: 400;
    color: var(--card-white);
    font-size: 30px;
    line-height: 54px;
    letter-spacing: 3px;
    text-transform: uppercase;
  }
</style>
</head>
<body>
<main class="canvas">

  <section class="card card--front" aria-label="Business card front">
    <svg class="front-stripes" viewBox="0 0 661 393" aria-hidden="true">
      <polygon class="stripe--blue" points="318,393 414,393 661,52 661,0 603,0"/>
      <polygon class="stripe--grey" points="461,393 661,393 661,121"/>
    </svg>

    <div class="contact">
      <h1 class="contact__name">Peter Hollis</h1>
      <p class="contact__title">Project Manager</p>
      <div class="contact__lines">
        <p class="contact__line">
          <svg class="contact__icon" viewBox="0 0 16 16" aria-hidden="true">
            <path d="M3.6 1.2l2.2 2.6c.3.4.3.9 0 1.3L4.7 6.4c.9 2 2.6 3.8 4.8 4.9l1.3-1.1c.4-.3.9-.3 1.3 0l2.6 2.2c.4.3.4.9.1 1.3l-1.2 1.3c-.5.5-1.3.7-2 .4C6.5 13.8 2.4 9.7.8 4.6c-.2-.7 0-1.5.5-2l1.2-1.3c.3-.4.8-.4 1.1-.1z"/>
            <path d="M9.5 1.5a5 5 0 0 1 5 5h-1.3a3.7 3.7 0 0 0-3.7-3.7z M9.5 4a2.5 2.5 0 0 1 2.5 2.5h-1.2a1.3 1.3 0 0 0-1.3-1.3z"/>
          </svg>
          (+34) 612 738 104
        </p>
        <p class="contact__line">
          <svg class="contact__icon" viewBox="0 0 16 16" aria-hidden="true">
            <path d="M1 3h14v10H1z M1.8 3.8L8 8.8l6.2-5" fill="none" stroke="var(--brand-blue)" stroke-width="0"/>
            <path d="M1 3h14L8 8.5z M1 4.3l4.6 3.9L1 12.3z M15 4.3v8L10.4 8.2z M6.5 9l1.5 1.2L9.5 9 14.6 13H1.4z"/>
          </svg>
          peter@quorvane.net
        </p>
      </div>
      <p class="contact__company">Quorvane Management</p>
      <p class="contact__address">Meridel Tower, Office 22 - KRB</p>
      <p class="contact__city">Palma de Mallorca</p>
    </div>
  </section>

  <section class="card card--back" aria-label="Business card back">
    <div class="back-field" role="img" aria-label="Blue background with a subtle repeating pattern of light triangles"></div>
    <p class="wordmark">Quorvane<br>Management</p>
  </section>

</main>
</body>
</html>
```